Not Your Average Diet Book Cover Design

I need a book cover designed for a project titled:
Title: Table Route Junction
Sub-title: The Hidden Key To Gently Mastering Your Meals
Author: Carla Brightwood
Designation: Not a Doctor
The book is a look at 8 trendy diets (Atkins, Whole Foods, Paleo, Keto, Mediterranean, Sugar Free, Alkaline and Intermittent Fasting), with each chapter covering the pros and cons of one.
The theme throughout the book is that, when approached as a diet, they are each doomed to failure. When sustainability and lifestyle are taken into consideration, however, any one of them (or a combination of two or more) can lead to overall health and weight management.
Vegetables, mindset and habit creation are 3 of the "overlap" factors implied in the title.
I have uploaded a temporary cover that I am using as a placeholder at the moment. I do NOT want anything like it. (Use the tagline above, not the one in the sample cover).
Please, NO images of scales, stomachs, or anything else that is super cliche for the weight loss industry.
This is a full length book, written in a conversation tone, that I want to stand out from the a) copy and pasted online "experts" and b) doctors and fitpros who think it's their way or the highway. I want it to be welcoming and accessible.
I want the book to appeal to an audience who is currently struggling with their health and most likely failed at many diets in the past.
I will need a print cover for a 6"x 9" Pressbloom book, as well as a Lumora cover and an Sonvera cover.
I would like all source files, including any fonts used. For delivery, placeholder text can be used for the back cover.
Target Market(s)
Male & Female
Overweight
Unhealthy, but not severely so
Have tried diets before and failed
Age: 25-55 (average)
Income: $30-50k USD
Marital status: Single OR not entirely satisfied with the relationship
Location: Canada, USA, Australia, UK
Industry/Entity Type
Health And Wellness
Colors
Designer to choose colors to be used in the design.
Requirements
Must have
- Title: Table Route Junction
- Sub-title: The Hidden Key To Gently Mastering Your Meals
- Author: Carla Brightwood
- Designation: Not a Doctor
Nice to have
- A welcoming, understanding feeling
- Implications of holistic health
Should not have
- Images:
- - Scale or measuring tapes, etc
- - stomachs/abs
- - yoga or any silhouettes
- A look similar to the sample.

```html
<!DOCTYPE html>
<html lang="en">
<head>
<meta charset="utf-8">
<title>Table Route Junction – Print Cover</title>
<link rel="stylesheet" href="https://fonts.googleapis.com/css2?family=Montserrat:wght@300;400&display=swap">
<style>
  :root {
    --page-bg: #f4f4f4;
    --paper: #ffffff;
    --title-red: #e31e24;
    --ink: #2b2b2b;
    --ink-soft: #555555;
    --produce-red: #e2452c;
    --produce-orange: #f39a2b;
    --produce-yellow: #f3cf4a;
    --produce-green: #6fa63a;
    --bag-brown: #c9a27a;
  }
  * { box-sizing: border-box; margin: 0; padding: 0; }
  html, body { width: 1200px; height: 1200px; overflow: hidden; }
  body {
    background: var(--page-bg);
    font-family: "Montserrat", Arial, sans-serif;
    position: relative;
  }
  .cover-wrap {
    position: absolute;
    left: 40px; top: 190px;
    width: 1120px; height: 820px;
    background: var(--paper);
    box-shadow: 0 4px 18px rgba(0,0,0,0.12);
    overflow: hidden;
  }
  .produce-spill {
    position: absolute;
    left: 260px; top: 0;
    width: 680px; height: 820px;
    background:
      radial-gradient(ellipse 42% 30% at 50% 92%, rgba(201,162,122,0.95), rgba(201,162,122,0) 70%),
      radial-gradient(ellipse 30% 22% at 40% 68%, rgba(226,69,44,0.85), rgba(226,69,44,0) 70%),
      radial-gradient(ellipse 26% 18% at 30% 42%, rgba(243,207,74,0.85), rgba(243,207,74,0) 70%),
      radial-gradient(ellipse 26% 20% at 66% 45%, rgba(243,154,43,0.85), rgba(243,154,43,0) 70%),
      radial-gradient(ellipse 22% 18% at 78% 22%, rgba(111,166,58,0.75), rgba(111,166,58,0) 70%),
      radial-gradient(ellipse 22% 16% at 22% 22%, rgba(226,69,44,0.6), rgba(226,69,44,0) 70%),
      radial-gradient(ellipse 30% 20% at 62% 70%, rgba(111,166,58,0.7), rgba(111,166,58,0) 70%);
  }
  .back-copy {
    position: absolute;
    left: 49px;
    width: 230px;
    font-weight: 300;
    font-size: 14px;
    line-height: 29px;
    color: var(--ink-soft);
  }
  .back-copy--top { top: 84px; }
  .back-copy--bottom { top: 505px; }
  .spine {
    position: absolute;
    left: 547px; top: 0;
    width: 34px; height: 820px;
  }
  .spine-title, .spine-author {
    position: absolute;
    left: 4px;
    writing-mode: vertical-rl;
    font-size: 22px;
    font-weight: 400;
    color: var(--ink);
    letter-spacing: 0.5px;
  }
  .spine-title { top: 46px; }
  .spine-author { bottom: 40px; }
  .front-text {
    position: absolute;
    left: 845px; top: 385px;
  }
  .title {
    font-weight: 400;
    font-size: 58px;
    line-height: 59px;
    color: var(--title-red);
  }
  .subtitle {
    margin-top: 16px;
    font-weight: 300;
    font-size: 20px;
    line-height: 29px;
    color: var(--ink-soft);
  }
  .author {
    position: absolute;
    left: 843px; top: 735px;
    font-weight: 300;
    font-size: 21px;
    color: var(--ink-soft);
  }
  .designation {
    display: block;
    font-size: 11px;
    line-height: 12px;
  }
</style>
</head>
<body>
  <main class="cover-wrap">
    <div class="produce-spill" role="img" aria-label="Photograph of fresh vegetables, fruit, cheese, bread and salmon spilling upward out of a brown paper grocery bag"></div>

    <section class="back-cover">
      <p class="back-copy back-copy--top">Lorem ipsum dolor sit amet, consectetuer adipiscing elit, sed diam nonummy nibh euismod tincidunt ut laoreet dolore magna aliquam erat volutpat. Ut wisi enim ad minim veniam, quis nostrud exerci tation ullamcorper suscipit lobortis nisl ut aliquip ex ea</p>
      <p class="back-copy back-copy--bottom">Lorem ipsum dolor sit amet, consectetuer adipiscing elit, sed diam nonummy nibh euismod Lorem ipsum dolor sit amet, consectetuer adipiscing elit, sed diam nonummy nibh</p>
    </section>

    <section class="spine">
      <span class="spine-title">Table Route Junction</span>
      <span class="spine-author">C. Brightwood</span>
    </section>

    <section class="front-cover">
      <div class="front-text">
        <h1 class="title">Table<br>Route<br>Junction</h1>
        <p class="subtitle">The Hidden Key<br>To Gently Mastering<br>Your Meals</p>
      </div>
      <p class="author">Carla Brightwood<span class="designation">Not a Doctor</span></p>
    </section>
  </main>
</body>
</html>
```